ORVAN TECH LTD

going to a headteacher conference need a sign to show our services:
www.orvan-tech.co.uk
will attach a leaflet showing some more information.

Services:
IT Support
Web Design
Data Cabling (Fibre/Cat6)
Broadband
Hardware sales
WIFI
CCTV
Audio Visual
Door Access System
VOIP Telephone

```html
<!DOCTYPE html>
<html lang="en">
<head>
<meta charset="utf-8">
<title>Orvan Tech – Roll-up Banner</title>
<link href="https://fonts.googleapis.com/css2?family=Orbitron:wght@700;900&family=Poppins:wght@400;500;600;700&display=swap" rel="stylesheet">
<style>
  :root{
    --brand-blue:#1a6bb8;
    --deep-blue:#123d7e;
    --panel-blue:#1d4f9c;
    --navy:#0f2f66;
    --orange:#f07b3c;
    --white:#ffffff;
    --ink:#222;
  }
  html,body{margin:0;padding:0;width:1200px;height:2400px;overflow:hidden;background:var(--white);}
  .banner{position:relative;width:1200px;height:2400px;overflow:hidden;font-family:"Poppins",sans-serif;background:var(--white);}
  .lower-panel{position:absolute;left:0;top:1075px;width:1200px;height:1325px;
    background:radial-gradient(ellipse at 50% 40%, #2a62b0 0%, var(--panel-blue) 45%, var(--deep-blue) 100%);}

  .brand{position:absolute;top:110px;left:0;width:1200px;text-align:center;}
  .brand-name{font-family:"Orbitron",sans-serif;font-weight:900;font-size:92px;color:var(--brand-blue);letter-spacing:4px;line-height:1;}

  .headline{position:absolute;left:0;width:1200px;text-align:center;font-family:"Orbitron",sans-serif;font-weight:900;line-height:1;margin:0;}
  .headline-education{top:338px;font-size:112px;color:var(--brand-blue);letter-spacing:2px;}
  .headline-support{top:448px;font-size:112px;color:var(--brand-blue);letter-spacing:6px;}
  .headline-install{top:548px;font-size:64px;color:var(--orange);letter-spacing:3px;}
  .tag-box{position:absolute;left:204px;top:625px;width:793px;height:62px;background:var(--navy);
    color:var(--white);font-size:40px;font-weight:500;letter-spacing:9px;display:flex;align-items:center;justify-content:center;}
  .tag-shadow{position:absolute;left:220px;top:692px;width:760px;height:18px;border-radius:50%;
    background:radial-gradient(ellipse at center, rgba(0,0,0,.35) 0%, rgba(0,0,0,0) 70%);}

  .photo-frame{position:absolute;left:0;top:0;width:1200px;height:2400px;pointer-events:none;}
  .photo{position:absolute;left:186px;top:754px;width:820px;height:582px;box-sizing:border-box;
    border:8px solid var(--white);border-radius:90px 0 90px 90px;
    background:linear-gradient(135deg,#5b6c7e 0%,#8a9bab 35%,#7a3a35 60%,#c8b46a 100%);}

  .services-rule{position:absolute;left:0;top:0;}
  .services-title{position:absolute;left:330px;top:1420px;width:544px;height:54px;background:var(--orange);
    color:var(--white);font-weight:700;font-size:36px;letter-spacing:11px;display:flex;align-items:center;justify-content:center;}

  .service{position:absolute;width:240px;margin-left:-120px;text-align:center;color:var(--white);}
  .service svg{display:block;margin:0 auto;}
  .service-label{font-size:32px;line-height:1.18;margin-top:10px;}

  .cta-box{position:absolute;left:231px;top:2066px;width:752px;height:57px;background:var(--orange);
    color:var(--navy);font-weight:700;font-size:38px;letter-spacing:9px;display:flex;align-items:center;justify-content:center;}
  .phone{position:absolute;left:0;top:2160px;width:1200px;display:flex;align-items:center;justify-content:center;gap:18px;
    color:var(--white);font-weight:700;font-size:112px;line-height:1;letter-spacing:-1px;}
  .website{position:absolute;left:0;top:2262px;width:1200px;text-align:center;color:var(--white);
    font-weight:600;font-size:50px;letter-spacing:11px;}
</style>
</head>
<body>
<main class="banner">
  <div class="lower-panel"></div>

  <header class="brand">
    <div class="brand-name">ORVAN TECH</div>
  </header>

  <h1 class="headline headline-education">EDUCATION</h1>
  <h2 class="headline headline-support">SUPPORT</h2>
  <h2 class="headline headline-install">AND INSTALLATION</h2>
  <div class="tag-box">OF ALL TECHNOLOGIES</div>
  <div class="tag-shadow"></div>

  <svg class="photo-frame" width="1200" height="2400" viewBox="0 0 1200 2400" aria-hidden="true">
    <path d="M1048 808 V1280 A76 76 0 0 1 972 1356 H283" fill="none" stroke="var(--orange)" stroke-width="40"/>
  </svg>
  <div class="photo" role="img" aria-label="Photo of a pupil wearing a virtual reality headset in a classroom"></div>

  <svg class="services-rule" width="1200" height="2400" viewBox="0 0 1200 2400" aria-hidden="true">
    <path d="M179 1530 V1448 H1024 V1530" fill="none" stroke="var(--orange)" stroke-width="3"/>
  </svg>
  <div class="services-title">OUR SERVICES</div>

  <!-- Row 1 -->
  <div class="service" style="left:179px;top:1524px;">
    <svg width="116" height="104" viewBox="0 0 116 104"><polygon points="29,2 87,2 114,52 87,102 29,102 2,52" fill="var(--orange)"/><polygon points="33,10 83,10 106,52 83,94 33,94 10,52" fill="none" stroke="#fff" stroke-width="2"/>
      <rect x="40" y="36" width="36" height="32" rx="3" fill="none" stroke="#fff" stroke-width="3"/><path d="M32 44h8M32 60h8M76 44h8M76 60h8M48 28v8M68 28v8M48 68v8M68 68v8" stroke="#fff" stroke-width="3"/></svg>
    <div class="service-label">IT<br>Support</div>
  </div>
  <div class="service" style="left:389px;top:1524px;">
    <svg width="116" height="104" viewBox="0 0 116 104"><polygon points="29,2 87,2 114,52 87,102 29,102 2,52" fill="var(--orange)"/><polygon points="33,10 83,10 106,52 83,94 33,94 10,52" fill="none" stroke="#fff" stroke-width="2"/>
      <rect x="32" y="30" width="52" height="40" rx="3" fill="none" stroke="#fff" stroke-width="3"/><path d="M32 40h52" stroke="#fff" stroke-width="3"/><text x="58" y="62" fill="#fff" font-size="14" font-family="Poppins,sans-serif" text-anchor="middle">www</text></svg>
    <div class="service-label">Web<br>Design</div>
  </div>
  <div class="service" style="left:575px;top:1524px;">
    <svg width="116" height="104" viewBox="0 0 116 104"><polygon points="29,2 87,2 114,52 87,102 29,102 2,52" fill="var(--orange)"/><polygon points="33,10 83,10 106,52 83,94 33,94 10,52" fill="none" stroke="#fff" stroke-width="2"/>
      <rect x="32" y="36" width="44" height="20" rx="3" fill="none" stroke="#fff" stroke-width="3"/><path d="M76 44l10-4v16l-10-4M54 56v14H42" fill="none" stroke="#fff" stroke-width="3"/></svg>
    <div class="service-label">CCTV</div>
  </div>
  <div class="service" style="left:803px;top:1524px;">
    <svg width="116" height="104" viewBox="0 0 116 104"><polygon points="29,2 87,2 114,52 87,102 29,102 2,52" fill="var(--orange)"/><polygon points="33,10 83,10 106,52 83,94 33,94 10,52" fill="none" stroke="#fff" stroke-width="2"/>
      <rect x="32" y="56" width="52" height="14" rx="3" fill="none" stroke="#fff" stroke-width="3"/><path d="M74 56V30M46 44a16 16 0 0 1 24 0M50 49a9 9 0 0 1 16 0" fill="none" stroke="#fff" stroke-width="3"/></svg>
    <div class="service-label">Broadband</div>
  </div>
  <div class="service" style="left:1028px;top:1524px;">
    <svg width="116" height="104" viewBox="0 0 116 104"><polygon points="29,2 87,2 114,52 87,102 29,102 2,52" fill="var(--orange)"/><polygon points="33,10 83,10 106,52 83,94 33,94 10,52" fill="none" stroke="#fff" stroke-width="2"/>
      <rect x="36" y="28" width="30" height="48" rx="4" fill="none" stroke="#fff" stroke-width="3"/><path d="M44 38h14M44 46h14M44 54h14" stroke="#fff" stroke-width="3"/><circle cx="51" cy="66" r="4" fill="#fff"/><path d="M72 40a10 10 0 0 1 0 16M78 34a18 18 0 0 1 0 28" fill="none" stroke="#fff" stroke-width="3"/></svg>
    <div class="service-label">Door<br>Access<br>System</div>
  </div>

  <!-- Row 2 -->
  <div class="service" style="left:179px;top:1776px;">
    <svg width="116" height="104" viewBox="0 0 116 104"><polygon points="29,2 87,2 114,52 87,102 29,102 2,52" fill="var(--orange)"/><polygon points="33,10 83,10 106,52 83,94 33,94 10,52" fill="none" stroke="#fff" stroke-width="2"/>
      <rect x="38" y="32" width="40" height="40" rx="3" fill="none" stroke="#fff" stroke-width="3"/><rect x="48" y="42" width="20" height="20" fill="none" stroke="#fff" stroke-width="2"/><path d="M46 26v6M58 26v6M70 26v6M46 72v6M58 72v6M70 72v6" stroke="#fff" stroke-width="3"/></svg>
    <div class="service-label">Hardware<br>sales</div>
  </div>
  <div class="service" style="left:389px;top:1776px;">
    <svg width="116" height="104" viewBox="0 0 116 104"><polygon points="29,2 87,2 114,52 87,102 29,102 2,52" fill="var(--orange)"/><polygon points="33,10 83,10 106,52 83,94 33,94 10,52" fill="none" stroke="#fff" stroke-width="2"/>
      <rect x="32" y="40" width="52" height="32" rx="3" fill="none" stroke="#fff" stroke-width="3"/><path d="M40 40V30h36v10M42 56h8M54 56h8M66 56h8" fill="none" stroke="#fff" stroke-width="3"/></svg>
    <div class="service-label">Data<br>Cabling<br>(Fibre/Cat6)</div>
  </div>
  <div class="service" style="left:622px;top:1776px;">
    <svg width="116" height="104" viewBox="0 0 116 104"><polygon points="29,2 87,2 114,52 87,102 29,102 2,52" fill="var(--orange)"/><polygon points="33,10 83,10 106,52 83,94 33,94 10,52" fill="none" stroke="#fff" stroke-width="2"/>
      <rect x="34" y="30" width="36" height="30" rx="3" fill="none" stroke="#fff" stroke-width="3"/><path d="M48 38l10 7-10 7z" fill="#fff"/><path d="M76 50v14a8 8 0 0 1-16 0M68 72v6" fill="none" stroke="#fff" stroke-width="3"/></svg>
    <div class="service-label">Audio<br>Visual</div>
  </div>
  <div class="service" style="left:818px;top:1776px;">
    <svg width="116" height="104" viewBox="0 0 116 104"><polygon points="29,2 87,2 114,52 87,102 29,102 2,52" fill="var(--orange)"/><polygon points="33,10 83,10 106,52 83,94 33,94 10,52" fill="none" stroke="#fff" stroke-width="2"/>
      <path d="M40 42a26 26 0 0 1 36 0M46 48a17 17 0 0 1 24 0M52 54a8 8 0 0 1 12 0" fill="none" stroke="#fff" stroke-width="3"/><rect x="36" y="60" width="44" height="16" rx="3" fill="none" stroke="#fff" stroke-width="3"/><text x="58" y="73" fill="#fff" font-size="11" font-weight="700" font-family="Poppins,sans-serif" text-anchor="middle">WIFI</text></svg>
    <div class="service-label">WIFI</div>
  </div>
  <div class="service" style="left:1028px;top:1776px;">
    <svg width="116" height="104" viewBox="0 0 116 104"><polygon points="29,2 87,2 114,52 87,102 29,102 2,52" fill="var(--orange)"/><polygon points="33,10 83,10 106,52 83,94 33,94 10,52" fill="none" stroke="#fff" stroke-width="2"/>
      <path d="M38 44c0 14 12 28 26 30l6-8-8-6-5 4c-5-3-8-7-10-12l4-5-6-8z" fill="none" stroke="#fff" stroke-width="3"/><rect x="60" y="26" width="28" height="16" rx="8" fill="none" stroke="#fff" stroke-width="2"/><text x="74" y="38" fill="#fff" font-size="9" font-weight="700" font-family="Poppins,sans-serif" text-anchor="middle">VOIP</text></svg>
    <div class="service-label">VOIP<br>Telephone</div>
  </div>

  <div class="cta-box">CONTACT US TODAY!</div>
  <div class="phone">
    <svg width="82" height="82" viewBox="0 0 82 82" aria-hidden="true"><circle cx="41" cy="41" r="39" fill="var(--white)"/><circle cx="41" cy="41" r="33" fill="#1e8ce6"/><path d="M27 30c2 14 11 23 25 26l5-7-8-6-5 3c-4-2-7-5-9-9l3-5-6-8z" fill="var(--navy)"/></svg>
    <span>0161 555 0142</span>
  </div>
  <div class="website">www.orvan-tech.co.uk</div>
</main>
</body>
</html>
```